The Wardrobe Sage needs a business card

The wardrobe sage is a lead generation service serving the Custom Closet industry.

Here is the basic card information:

The Wardrobe Sage
Dorian Pettigrew
Owner/CEO
Cedar Hollow, NC
704-318-5527 Cell
Email: dpettigrew@TheWardrobeSage.com

Additional information for the card:

"High quality, flat rate lead generation exclusively for the custom closet industry"

Bullet points for the back:

- Low fixed cost
- Easy to budget
- Guaranteed qualified Leeds
- Exclusivity per city

Logo attached, head shot attached. Photos of closet systems attached

```html
<!DOCTYPE html>
<html lang="en">
<head>
<meta charset="utf-8">
<title>The Wardrobe Sage — Business Card</title>
<link rel="stylesheet" href="https://fonts.googleapis.com/css2?family=Montserrat:ital,wght@0,400;0,500;0,700;1,400&display=swap">
<style>
  :root {
    --ink-grey: #58595b;
    --text-grey: #4d4d4f;
    --brand-brown: #a3622c;
    --card-white: #ffffff;
    --page-bg: #efefef;
    --interior-light: #f3f3f3;
    --interior-mid: #e3e3e3;
  }
  * { box-sizing: border-box; margin: 0; padding: 0; }
  html, body {
    width: 1200px; height: 1200px; overflow: hidden;
    background: var(--page-bg);
    font-family: "Montserrat", Arial, sans-serif;
  }
  .card {
    position: absolute; left: 178px;
    width: 844px; height: 497px;
    background: var(--card-white);
    box-shadow: 0 6px 18px rgba(0,0,0,0.18);
    overflow: hidden;
  }
  .card--front { top: 71px; }
  .card--back { top: 638px; }

  .front-shapes, .back-shapes { position: absolute; inset: 0; }

  .headshot {
    position: absolute; left: 648px; top: 89px;
    width: 114px; height: 114px; border-radius: 50%;
    background: radial-gradient(circle at 50% 40%, #6b5a50 0%, #3a3a3c 60%, #1f2024 100%);
  }

  .wordmark {
    position: absolute; display: flex; align-items: center; gap: 10px;
    font-weight: 700; color: var(--brand-brown);
    white-space: nowrap;
  }
  .wordmark__dot {
    width: 14px; height: 14px; border-radius: 50%;
    background: var(--brand-brown);
  }
  .card--front .wordmark { left: 64px; top: 155px; font-size: 30px; }

  .tagline {
    position: absolute; left: 64px; top: 213px;
    font-style: italic; font-size: 17px; line-height: 24px;
    color: var(--text-grey);
  }

  .contact-list {
    position: absolute; left: 64px; top: 320px; list-style: none;
  }
  .contact-list li {
    display: flex; align-items: center; gap: 14px;
    height: 32.5px; font-size: 19.5px; color: var(--text-grey);
  }
  .contact-list svg { width: 20px; height: 20px; flex: none; }

  .person {
    position: absolute; right: 55px; top: 322px; text-align: right;
  }
  .person__name {
    font-size: 22px; font-weight: 700; letter-spacing: 1.2px;
    color: var(--ink-grey); text-transform: uppercase;
  }
  .person__name span { color: var(--brand-brown); }
  .person__role { font-size: 19px; color: var(--text-grey); margin-top: 4px; }

  .interior-photo {
    position: absolute; inset: 0;
    background: linear-gradient(100deg, var(--interior-mid) 0%, var(--interior-light) 45%, #f8f8f8 70%, var(--interior-mid) 100%);
  }
  .shelving-photo {
    position: absolute; left: 0; top: 0; width: 236px; height: 100%;
    background: var(--brand-brown);
  }

  .benefit-list {
    position: absolute; left: 70px; top: 179px; list-style: none;
  }
  .benefit-list li {
    height: 38.5px; font-size: 17px; font-weight: 700;
    letter-spacing: 0.6px; color: #ffffff; text-transform: uppercase;
  }

  .card--back .wordmark { left: 520px; top: 232px; font-size: 28px; }
</style>
</head>
<body>

<section class="card card--front" aria-label="Business card front">
  <svg class="front-shapes" viewBox="0 0 844 497" aria-hidden="true">
    <rect x="0" y="62" width="185" height="17" fill="var(--ink-grey)"/>
    <path d="M232 70.5 H705 A75.5 75.5 0 0 1 705 221.5" fill="none" stroke="var(--ink-grey)" stroke-width="17"/>
    <rect x="0" y="445" width="380" height="26" fill="var(--ink-grey)"/>
    <rect x="380" y="445" width="464" height="26" fill="var(--brand-brown)"/>
  </svg>

  <div class="headshot" role="img" aria-label="Headshot portrait of Dorian Pettigrew"></div>

  <div class="wordmark"><span class="wordmark__dot"></span>The Wardrobe Sage</div>

  <p class="tagline">High quality, flat rate lead generation<br>exclusively for the custom closet industry</p>

  <ul class="contact-list">
    <li>
      <svg viewBox="0 0 20 20" aria-hidden="true"><rect x="5" y="1.5" width="10" height="17" rx="1.8" fill="none" stroke="var(--brand-brown)" stroke-width="1.8"/><line x1="8.5" y1="15.5" x2="11.5" y2="15.5" stroke="var(--brand-brown)" stroke-width="1.6"/></svg>
      704-318-5527
    </li>
    <li>
      <svg viewBox="0 0 20 20" aria-hidden="true"><rect x="1.5" y="4" width="17" height="12" fill="var(--brand-brown)"/><path d="M1.5 4 L10 11 L18.5 4" fill="none" stroke="#fff" stroke-width="1.4"/></svg>
      dpettigrew@TheWardrobeSage.com
    </li>
    <li>
      <svg viewBox="0 0 20 20" aria-hidden="true"><path d="M10 1.5 a5.5 5.5 0 0 1 5.5 5.5 c0 4 -5.5 9 -5.5 9 s-5.5 -5 -5.5 -9 a5.5 5.5 0 0 1 5.5 -5.5z" fill="none" stroke="var(--brand-brown)" stroke-width="1.8"/><circle cx="10" cy="7" r="1.8" fill="var(--brand-brown)"/><line x1="4" y1="18.5" x2="16" y2="18.5" stroke="var(--brand-brown)" stroke-width="1.6"/></svg>
      Cedar Hollow, NC
    </li>
  </ul>

  <div class="person">
    <p class="person__name">Dorian <span>Pettigrew</span></p>
    <p class="person__role">Owner/CEO</p>
  </div>
</section>

<section class="card card--back" aria-label="Business card back">
  <div class="interior-photo" role="img" aria-label="Faded photo of a bright custom closet interior"></div>
  <div class="shelving-photo" role="img" aria-label="Closet shelving photo with brown tint"></div>
  <svg class="back-shapes" viewBox="0 0 844 497" aria-hidden="true">
    <path d="M235 1 A247.5 247.5 0 0 1 235 496 Z" fill="var(--ink-grey)"/>
    <path d="M234 51 A197.5 197.5 0 0 1 234 446 Z" fill="var(--brand-brown)"/>
  </svg>

  <ul class="benefit-list">
    <li>Low fixed cost</li>
    <li>Easy to budget</li>
    <li>Guaranteed qualified leeds</li>
    <li>Exclusivity per city</li>
  </ul>

  <div class="wordmark"><span class="wordmark__dot"></span>The Wardrobe Sage</div>
</section>

</body>
</html>
```